Indie author needs a minimalist book cover

I need a book cover for my latest book on personal finance and investing. The book is called, "The Quiet Margin: Lessons on Steady Wealth, Calm Careers, and a Full Table". This is volume one of a three part series on the FI/RE movement, which stands for 'Financial Independence/Retire Early'. This book is on the foundational principles of FI/RE and details the specific steps that these 'Quiet Margin' involved in this community have done to position themselves to retire from paid work and live the life of their dreams - many only in their 20's, 30's and early 40's.

Title: The Quiet Margin
Author: RK Brenner
Volume 1: Foundations
Book dimensions: 6"x9"

Book Blurb (for back cover):

Let's face it, no one wants to be different. But sometimes following the 'normal' crowd gets you no further than that crowd.

When it comes to money, the normal crowd is your typical consumer. Deep in debt, struggling to make ends meet, but still spending money on the newest 'thing' that just came out.

But there's another group that's been forming - right on the fringes of the personal finance world. I call them The Quiet Margin. This book is about these superheroes of personal finance.

In it, you will learn:
• Who The Quiet Margin are and what is this FI/RE Movement they are apart of
• What basic strategy they use to control their money
• How they became debt-free - and how you can join them
• How to use the Tidewell Lever to help you really move the needle towards financial independence
• How to diversify your income with a side-hustle and which one to choose
• The money outlier savings plan that will allow you to reach financial independence in ten years or less

This first book in The Quiet Margin series is about building a solid foundation so you and your family can become Quiet Margin, reach financial freedom, retire early, and live a rich life.

Target Market(s)

Individuals looking to take control of their money, reach financial independence, and retire early.

Font styles to use
Sans Serif
Other font styles liked:
• Arvo

Colors

Designer to choose colors to be used in the design.

Requirements
Must have
• A minimalist design (see examples), the title of the book, my author name, and the volume number and name (see below).
• My vision for the cover is to have a way to represent an 'outlier' in a simple, minimalistic way. I'm not set on any specific design - I'm open to what the designers come up with; I don't want to hold back anyone's creativity.
• Title: The Quiet Margin
• Author: RK Brenner
• Volume 1: Foundations
• Book Blurb (for back cover):
• Let's face it, no one wants to be different. But sometimes following the 'normal' crowd gets you no further than that crowd.
• When it comes to money, the normal crowd is your typical consumer. Deep in debt, struggling to make ends meet, but still spending money on the newest 'thing' that just came out.
• But there's another group that's been forming - right on the fringes of the personal finance world. I call them The Quiet Margin. This book is about these superheroes of personal finance.
• In it, you will learn:
• • Who The Quiet Margin are and what is this FI/RE Movement they are apart of
• • What basic strategy they use to control their money
• • How they became debt-free - and how you can join them
• • How to use the Tidewell Lever to help you really move the needle towards financial independence
• • How to diversify your income with a side-hustle and which one to choose
• • The money outlier savings plan that will allow you to reach financial independence in ten years or less
• This first book in The Quiet Margin series is about building a solid foundation so you and your family can become Quiet Margin, reach financial freedom, retire early, and live a rich life.
Nice to have
• The subtitle - but only if it's not too crowded. Like I said before, I'm more interested in maintaining a minimalist aesthetic.
• The subtitle is: "Lessons on Steady Wealth, Calm Careers, And A Full Table"
Should not have
• Too many colors or objects on the cover.

```html
<!DOCTYPE html>
<html lang="en">
<head>
<meta charset="utf-8">
<title>The Quiet Margin — Volume 1: Foundations</title>
<link rel="stylesheet" href="https://fonts.googleapis.com/css2?family=Arvo:ital,wght@0,400;0,700;1,400&display=swap">
<style>
  :root {
    --paper: #ffffff;
    --tile-grey: #e8e8e9;
    --tile-line: #d3d3d5;
    --accent: #00aeef;
    --piece-blue: #29abe2;
    --ink: #111111;
  }
  html, body {
    margin: 0;
    padding: 0;
    overflow: hidden;
    background: var(--paper);
  }
  .cover {
    position: relative;
    width: 800px;
    height: 1200px;
    overflow: hidden;
    background: var(--paper);
    font-family: "Arvo", serif;
  }
  .crowd-field {
    position: absolute;
    left: 0;
    top: 0;
    width: 800px;
    height: 490px;
  }
  .outlier-piece {
    position: absolute;
    left: 306px;
    top: 680px;
    width: 112px;
    height: 124px;
    background: var(--piece-blue);
  }
  .title {
    position: absolute;
    left: 0;
    width: 822px;
    top: 536px;
    margin: 0;
    text-align: center;
    font-weight: 400;
    font-size: 58px;
    letter-spacing: 1px;
    line-height: 1;
    color: var(--accent);
  }
  .author {
    position: absolute;
    right: 133px;
    top: 620px;
    margin: 0;
    font-style: italic;
    font-size: 36px;
    line-height: 1;
    color: var(--ink);
  }
  .subtitle {
    position: absolute;
    left: 150px;
    width: 534px;
    top: 916px;
    margin: 0;
    text-align: center;
    font-style: italic;
    font-size: 23px;
    line-height: 29px;
    letter-spacing: 0.5px;
    color: var(--ink);
  }
  .volume-band {
    position: absolute;
    left: 0;
    top: 1059px;
    width: 800px;
    height: 141px;
    background: var(--accent);
  }
  .volume-label {
    position: absolute;
    left: 0;
    width: 800px;
    top: 57px;
    margin: 0;
    text-align: center;
    font-weight: 700;
    font-size: 24px;
    line-height: 1;
    color: var(--ink);
  }
</style>
</head>
<body>
  <main class="cover">
    <svg class="crowd-field" viewBox="0 0 800 490" role="img" aria-label="Grid of grey jigsaw pieces marked with dollar signs, with one piece missing">
      <path fill="var(--tile-grey)" d="M0 0 H800 V453 H0 Z M307 330 V453 H418 V330 Z" fill-rule="evenodd"/>
    </svg>

    <h1 class="title">The Quiet Margin</h1>
    <p class="author">RK Brenner</p>

    <div class="outlier-piece" role="img" aria-label="Single blue jigsaw piece with a dollar sign"></div>

    <p class="subtitle">Lessons on Steady Wealth, Calm Careers, And A Full Table</p>

    <footer class="volume-band">
      <p class="volume-label">Volume 1: Foundations</p>
    </footer>
  </main>
</body>
</html>
```